Varubo Highlands coffee needs bold, new coffee pack design

Having just developed a new logo (see attached file), we are now in the process of developing new coffee bag packaging designs. We are using a custom bag printer in the US, so the design will need will need to follow a specific art spec/template (which has also been uploaded). We will eventually need designs for two different coffee brands/types and two different size bags (essentially a 250g and 500g size). At this point, however, our goal is to develop a design for one size/coffee brand and from there work on variations for the others.
Updates

Project Deadline Extended
Reason: We are considering some small changes to the original design we outlined and want to allow extra time for current and new designers to make those tweaks. Thanks for your consideration of our coffee package project!

Hello, After reviewing some designs so far, and receiving additional feedback from test users in our market, we are making some changes to the template design. I have uploaded a new version of the template content, which has the following changes. 1. The two side panels are now without any text, but a visual design/pattern that you want to try there is still welcome. 2. The front and bag sections has been cleaned up a bit to have less text and more room for a visual design. 3. We would like to see stronger user of the following colors: red, yellow, black (which are Ugandan flag colors) and white. Some green as needed is allowed. 4. I have uploaded a map file showing Uganda including the Varubo region where the coffee comes from. Would like to incorporate this on the back side, ideally with a small Varubo Highlands logo pointing to the region in the bottom left in green or could even say something like "Home of Varubo Highlands Coffee.". Also the country should be titled "Uganda" to make that clear. With these changes, if you need more time on the design, let me know and we can look at extending the deadline. Thank you!

Hello, Although it is not showing just yet, we expect to have a one-week extension for this contest (so not ending on 29 September, but October 6). If you are working on a design, or re-design, please continue to do so as the contest will be extended. If you are interested in starting work, please do so. Thanks for your interest in our package design contest and I look forward to seeing your work soon. Doriel

Hello, Thank you to everyone who has submitted designs so far. We want to highlight two important items at this point: 1. Based on user feedback, we are changing the design considerations bit. The size and shape of the bags are not changing, but some of the creative content is. A new file has been uploaded entitled Coffee package content 250g size v3.pdf which details these changes. Please download and read that for updates. If you have any questions, please let me know. 2. Due to these changes, we are extending this contest for another week, so I'm hopeful you will have time to make changes and submit your new ideas! Thank you, Doriel

Target Market(s)

Varubo Highlands is a premium Ugandan coffee. We are targeting those drinkers who appreciate and seek out great coffee.

Industry/Entity Type

Printer

Font styles to use
Sans Serif

Colors
ec1f27
ffffff
9bcb3c
ffcf3e

Requirements
Must have
• The attached PDF file (coffee package content) design and content elements that need to be included. Designer has strong license to determine HOW they should be designed and shown. In terms of colors, would like to see strong use of red, black, yellow (Ugandan flag colors) and white. Green is also an option if needed.

The design file will need to follow specs that are detailed here:
http://www.pelmacrate.com/artwork_specs and be in the format shown in the uploaded file 5-8 oz Bag Template.pdf.
Nice to have
• Bag should be simple, but elegant. We did testing and found that too much information was distracting so we have pared down the design/content elements to the basics. Still, creative elements or patterns and overlays are very welcome.
Should not have
• The tone should be elegant and creative, but not hokey or too handmade looking. Watch the use of too many fonts and low-contrast colors with text on background.

```html
<!DOCTYPE html>
<html lang="en">
<head>
<meta charset="utf-8">
<title>Varubo Highlands – Coffee Bag Fronts</title>
<link rel="stylesheet" href="https://fonts.googleapis.com/css2?family=Jost:ital,wght@0,500;0,600;0,700;1,700&display=swap">
<style>
  :root {
    --backdrop: #e4e3e3;
    --bag-top: #f8eeec;
    --bag-blush: #e2b2a6;
    --bag-rose: #c98a78;
    --bag-rust: #a04f3a;
    --bag-earth: #6b3122;
    --bag-shadow: #2e1c17;
    --bag-base: #141010;
    --seal: rgba(255,255,255,0.45);
    --gusset: rgba(0,0,0,0.16);
    --brand-red: #b8242a;
    --brand-mark: #1e1a1a;
    --text-light: #ffffff;
    --dark-band: #b27638;
    --dark-band-tail: #8a5628;
    --light-band: #d1bb34;
    --light-band-tail: #a79125;
    --frame-grey: #55575b;
    --band-text-dark: #ffffff;
    --band-text-light: #3a3a3a;
  }
  * { box-sizing: border-box; margin: 0; padding: 0; }
  html, body {
    width: 1200px; height: 927px; overflow: hidden;
    background: var(--backdrop);
    font-family: "Jost", Arial, sans-serif;
  }
  .canvas { position: relative; width: 1200px; height: 927px; }

  .bag {
    position: absolute; top: 140px;
    width: 290px; height: 580px;
    overflow: hidden;
    background: linear-gradient(180deg,
      var(--bag-top) 0%,
      var(--bag-blush) 18%,
      var(--bag-rose) 32%,
      var(--bag-rust) 48%,
      var(--bag-earth) 64%,
      var(--bag-shadow) 82%,
      var(--bag-base) 100%);
  }
  .bag--dark  { left: 280px; }
  .bag--light { left: 655px; }

  .bag__seal {
    position: absolute; left: 0; right: 0; top: 0; height: 34px;
    background: linear-gradient(180deg, rgba(255,255,255,0.7), rgba(255,255,255,0.2));
    border-bottom: 1px solid var(--seal);
  }
  .bag__gusset {
    position: absolute; top: 34px; bottom: 0; width: 12px;
    background: linear-gradient(90deg, var(--gusset), transparent);
  }
  .bag__gusset--left { left: 0; }
  .bag__gusset--right { right: 0; transform: scaleX(-1); }

  .bag__scene {
    position: absolute; left: 12px; right: 12px; top: 110px; bottom: 40px;
    background:
      linear-gradient(172deg, transparent 0 30%, rgba(150,70,50,0.35) 30% 36%, transparent 36% 100%),
      linear-gradient(186deg, transparent 0 48%, rgba(90,40,28,0.35) 48% 55%, transparent 55% 100%),
      linear-gradient(176deg, transparent 0 66%, rgba(60,32,24,0.4) 66% 74%, transparent 74% 100%),
      linear-gradient(180deg, rgba(220,150,130,0.35), rgba(120,55,40,0.35) 50%, rgba(30,20,18,0.3));
  }

  .brand {
    position: absolute; left: 0; right: 0; top: 82px;
    display: flex; flex-direction: column; align-items: center; gap: 16px;
  }
  .brand__dot {
    width: 64px; height: 64px; border-radius: 50%;
    background: var(--brand-mark);
  }
  .brand__name {
    font-weight: 600; font-size: 23px; color: var(--brand-red);
    white-space: nowrap;
  }

  .roast {
    position: absolute; left: 50%; top: 356px;
    width: 184px; height: 60px; transform: translateX(-50%);
  }
  .roast__label { font-family: "Jost", Arial, sans-serif; font-weight: 600; font-size: 16px; }

  .tagline {
    position: absolute; left: 0; right: 0; top: 426px; text-align: center;
    color: var(--text-light); font-weight: 700; font-style: italic; font-size: 11px;
  }
  .weight {
    position: absolute; right: 28px; bottom: 28px;
    color: var(--text-light); font-weight: 500; font-size: 9px;
  }
</style>
</head>
<body>
<main class="canvas">

  <section class="bag bag--dark">
    <div class="bag__scene" role="img" aria-label="Painted view of terraced Ugandan highland hills fading into dark earth"></div>
    <div class="bag__seal"></div>
    <div class="bag__gusset bag__gusset--left"></div>
    <div class="bag__gusset bag__gusset--right"></div>
    <div class="brand">
      <span class="brand__dot"></span>
      <span class="brand__name">Varubo Highlands</span>
    </div>
    <svg class="roast" viewBox="0 0 184 60" aria-label="Dark Roast">
      <rect x="28" y="2" width="128" height="56" rx="6" fill="#ffffff" stroke="var(--frame-grey)" stroke-width="2"/>
      <rect x="33" y="7" width="118" height="46" rx="4" fill="none" stroke="var(--frame-grey)" stroke-width="1"/>
      <polygon points="0,18 20,18 20,44 0,44 8,31" fill="var(--dark-band-tail)"/>
      <polygon points="184,18 164,18 164,44 184,44 176,31" fill="var(--dark-band-tail)"/>
      <rect x="14" y="16" width="156" height="30" fill="var(--dark-band)"/>
      <text class="roast__label" x="92" y="37" text-anchor="middle" fill="var(--band-text-dark)">DARK ROAST</text>
    </svg>
    <p class="tagline">A bold, rich 100% Arabica roast.</p>
    <p class="weight">250g | 9oz</p>
  </section>

  <section class="bag bag--light">
    <div class="bag__scene" role="img" aria-label="Painted view of terraced Ugandan highland hills fading into dark earth"></div>
    <div class="bag__seal"></div>
    <div class="bag__gusset bag__gusset--left"></div>
    <div class="bag__gusset bag__gusset--right"></div>
    <div class="brand">
      <span class="brand__dot"></span>
      <span class="brand__name">Varubo Highlands</span>
    </div>
    <svg class="roast" viewBox="0 0 184 60" aria-label="Light Roast">
      <rect x="28" y="2" width="128" height="56" rx="6" fill="#ffffff" stroke="var(--frame-grey)" stroke-width="2"/>
      <rect x="33" y="7" width="118" height="46" rx="4" fill="none" stroke="var(--frame-grey)" stroke-width="1"/>
      <polygon points="0,18 20,18 20,44 0,44 8,31" fill="var(--light-band-tail)"/>
      <polygon points="184,18 164,18 164,44 184,44 176,31" fill="var(--light-band-tail)"/>
      <rect x="14" y="16" width="156" height="30" fill="var(--light-band)"/>
      <text class="roast__label" x="92" y="37" text-anchor="middle" fill="var(--band-text-light)">LIGHT ROAST</text>
    </svg>
    <p class="tagline">A bold, rich 100% Arabica roast.</p>
    <p class="weight">250g | 9oz</p>
  </section>

</main>
</body>
</html>
```